Design a nice single page website containing a link list

Hello,

you should design a nice single page website to replace the old website http://www.tovrella.de/

The company is running multiple flag shops. Your new website should only lead to a lot of other company websites. They are mentioned below. No link dropdowns please. We would like to see all links.

The company is offering flags. Big flags, but the special products are high quality diplomatic car flags. It is important, that people see, that it is about flags and specialy about car flags.

As customers are very international, the website should not contain unnecessary text. No text, no wrong languages.

You should implement links to:

Car Flag Shops: (pleaae don't use this as headline. Use symbols)
New Logo: Little car attached (without text below)
http://www.ridepennon.eu (english site payment in Euro)
http://us.ridepennon.eu (english site payment in USD)
http://fr.ridepennon.eu (french site payment in Euro)
http://es.ridepennon.eu (spanish site payment in Euro)
http://de.ridepennon.eu (germansite payment in Euro)

http://www.ridepennon.net (english site payment in USD)
http://www.ridepennant.co.uk (english site payment in british pounds)
http://www.wagen-wimpel.net (german site payment in Euro)
http://www.wagen-banner.at (austrian site payment in Euro)
http://www.wagen-wimpl.ch (german site payment in Swiss Franken)

Big flag shops: (pleaae don't use this as headline. Use symbols)
Logo: tovRella (attached incl. font) (black part of logo can also be made white)
(World map used next to the tovRella font attached)
http://www.tovrella.ne/ (english site payment in Euro)
http://fr.tovrella.net (french site payment in Euro)
http://es.tovrella.net (spanish site payment in Euro)
http://de.tovrella.net (german site payment in Euro)
http://it.tovrella.net (italian site payment in Euro)

Car flags product page: (pleaae don't use this as headline. Use symbols)
Logo: EnvoyPennon (attached incl. font)
http://www.envoy-pennon.com (english site)
http://fr.envoy-pennon.com (french site)
http://es.envoy-pennon.com (spanish site)
http://de.envoy-pennon.com (german site)

Please also add links to
English Blog
German Blog
4 language newsletter registration forms.

Also company data has to be added to the bottom of the page.
You could copy / paste from here:
http://www.ridepennon.eu/tovRella-GmbH

No additional links. No social icons.

General design:
Customers are, ambassoders, embassies, international organisiations.
Customers are powerful men, who want to show their power.
That's the reason, why they add this car flags to their car.

So colors should not be too soft. In the past we used colors like black and gold.
Completly black / dark background and bright white text is ok.

Most of our company prints have the kelvane arch in the background.
It would be good to include this also. (Image attached)

It is about a flag company. So don't forget to add big flags.
It would be also good to include an image like this:
http://de.pixvendra.com/id/38275016

Logos are available in high resolution. At the end you should mail us psd file with your winning design.

Please feel free to use all images you will find on the websites above.
If you need special images, please let me know, and we willt try to provide them.

Kind regards,

Dorian
Updates

Hello,
thanks for your feedback.Project payment is now committed.
Kind regards,
Lorenzo

Target Market(s)

World wide

Industry/Entity Type

Flag

Requirements
Must have
• Self explaining links to all the target pages.
Should not have
• unnecessary text. Domain names and logos with text are fine.
I think, we could avoid nearly all other text.

```html
<!DOCTYPE html>
<html lang="en">
<head>
<meta charset="utf-8">
<title>tovRella</title>
<link rel="stylesheet" href="https://fonts.googleapis.com/css2?family=Roboto+Condensed:wght@300&family=Hind:wght@400;500;600&family=Montserrat:wght@400&display=swap">
<style>
  :root {
    --white: #ffffff;
    --hero-dark: #2a1d12;
    --hero-mid: #6b5038;
    --hero-light: #a48868;
    --ink: #111111;
    --footer-text: #555555;
    --rule: #d6d6d6;
    --gold: #8a6d2c;
    --grey-mark: #9a9a9a;
    --video-dark: #1f3a2c;
    --video-mid: #3f6a52;
  }
  * { box-sizing: border-box; margin: 0; padding: 0; }
  html, body { width: 1200px; height: 1126px; overflow: hidden; background: var(--white); }
  .page { position: relative; width: 1200px; height: 1126px; font-family: "Hind", sans-serif; }

  .hero-photo {
    position: absolute; left: 0; top: 0; width: 1200px; height: 614px;
    background:
      radial-gradient(ellipse at 50% 35%, rgba(164,136,104,0.55), rgba(0,0,0,0) 60%),
      linear-gradient(180deg, var(--hero-mid) 0%, var(--hero-dark) 45%, var(--hero-mid) 80%, var(--hero-light) 100%);
  }

  .top-nav { position: absolute; top: 46px; left: 139px; right: 139px; height: 24px; }
  .nav-group { position: absolute; top: 0; display: flex; align-items: center; gap: 4px; color: var(--white); font-weight: 600; font-size: 15px; }
  .nav-group.newsletter { left: 0; }
  .nav-group.blog { right: 0; }
  .nav-group .label { margin-right: 8px; }
  .lang-flag { display: block; width: 14px; height: 9px; }

  .brand { position: absolute; left: 0; right: 0; top: 34px; text-align: center; color: var(--white); font-weight: 600; font-size: 40px; letter-spacing: 0.5px; }
  .brand .dot { display: inline-block; width: 12px; height: 12px; border-radius: 50%; background: var(--white); margin-left: 6px; vertical-align: middle; }

  .section-title { position: absolute; left: 0; right: 0; text-align: center; color: var(--white); font-family: "Roboto Condensed", sans-serif; font-weight: 300; }
  .welcome-title { top: 182px; font-size: 48px; }
  .title-rule { position: absolute; top: 209px; height: 1px; width: 216px; background: var(--white); }
  .title-rule.left { left: 278px; }
  .title-rule.right { left: 706px; }

  .site-list { position: absolute; top: 248px; left: 150px; right: 150px; text-align: center; color: var(--white); font-size: 16px; line-height: 23px; font-weight: 500; }
  .site-list p + p { margin-top: 21px; }
  .site-list a { color: var(--white); text-decoration: none; }
  .site-list .sep { margin: 0 8px; opacity: 0.7; }

  .video-title { top: 438px; font-size: 36px; }
  .video-frame { position: absolute; left: 482px; top: 494px; width: 236px; height: 231px; background: var(--white); padding: 10px; }
  .video-still { width: 217px; height: 217px; background: radial-gradient(circle at 40% 40%, var(--video-mid), var(--video-dark) 75%); position: relative; }
  .play-button { position: absolute; left: 65px; top: 66px; }

  .shop-logos { position: absolute; left: 140px; top: 780px; width: 920px; height: 160px; border-bottom: 1px solid var(--rule); display: flex; }
  .shop-logo { display: flex; align-items: center; justify-content: center; gap: 10px; text-decoration: none; font-weight: 600; }
  .shop-logo + .shop-logo { border-left: 1px solid var(--rule); }
  .shop-logo.envoy { font-size: 34px; color: var(--gold); width: 304px; }
  .shop-logo.ride { font-size: 36px; color: var(--ink); width: 314px; }
  .shop-logo.tov { font-size: 42px; color: var(--grey-mark); flex: 1; }
  .shop-logo .mark { width: 16px; height: 16px; background: var(--ink); }

  .footer { position: absolute; left: 0; right: 0; top: 968px; text-align: center; font-family: "Montserrat", sans-serif; font-size: 12px; color: var(--footer-text); }
  .footer-links { height: 22px; line-height: 22px; }
  .footer-links a { color: var(--footer-text); text-decoration: none; }
  .footer-links .sep { margin: 0 6px; }
  .footer-note { margin-top: 24px; line-height: 24px; }
</style>
</head>
<body>
<div class="page">
  <div class="hero-photo" role="img" aria-label="Sepia photograph of the kelvane arch"></div>

  <nav class="top-nav">
    <div class="nav-group newsletter">
      <span class="label">Newsletter</span>
      <svg class="lang-flag" viewBox="0 0 3 3" preserveAspectRatio="none" aria-label="German"><rect width="3" height="1" fill="#000"/><rect y="1" width="3" height="1" fill="#d00"/><rect y="2" width="3" height="1" fill="#fc0"/></svg>
      <svg class="lang-flag" viewBox="0 0 3 3" preserveAspectRatio="none" aria-label="English"><rect width="3" height="3" fill="#c8102e"/><rect x="1.2" width="0.6" height="3" fill="#fff"/><rect y="1.2" width="3" height="0.6" fill="#fff"/></svg>
      <svg class="lang-flag" viewBox="0 0 3 3" preserveAspectRatio="none" aria-label="French"><rect width="1" height="3" fill="#0055a4"/><rect x="1" width="1" height="3" fill="#fff"/><rect x="2" width="1" height="3" fill="#ef4135"/></svg>
      <svg class="lang-flag" viewBox="0 0 4 4" preserveAspectRatio="none" aria-label="Spanish"><rect width="4" height="4" fill="#c60b1e"/><rect y="1" width="4" height="2" fill="#ffc400"/></svg>
    </div>
    <div class="nav-group blog">
      <span class="label">Blog</span>
      <svg class="lang-flag" viewBox="0 0 3 3" preserveAspectRatio="none" aria-label="German"><rect width="3" height="1" fill="#000"/><rect y="1" width="3" height="1" fill="#d00"/><rect y="2" width="3" height="1" fill="#fc0"/></svg>
      <svg class="lang-flag" viewBox="0 0 3 3" preserveAspectRatio="none" aria-label="English"><rect width="3" height="3" fill="#c8102e"/><rect x="1.2" width="0.6" height="3" fill="#fff"/><rect y="1.2" width="3" height="0.6" fill="#fff"/></svg>
    </div>
  </nav>

  <div class="brand">tovRella<span class="dot"></span></div>

  <span class="title-rule left"></span>
  <h1 class="section-title welcome-title">Welcome</h1>
  <span class="title-rule right"></span>

  <div class="site-list">
    <p>
      <a href="http://www.envoy-pennon.com">www.envoy-pennon.com</a><span class="sep">|</span><a href="http://fr.envoy-pennon.com">fr.envoy-pennon.com</a><span class="sep">|</span><a href="http://es.envoy-pennon.com">es.envoy-pennon.com</a><span class="sep">|</span><a href="http://de.envoy-pennon.com">de.envoy-pennon.com</a><br>
      <a href="http://www.tovrella.ne/">www.tovrella.ne</a><span class="sep">|</span><a href="http://fr.tovrella.net">fr.tovrella.net</a><span class="sep">|</span><a href="http://es.tovrella.net">es.tovrella.net</a><span class="sep">|</span><a href="http://de.tovrella.net">de.tovrella.net</a><span class="sep">|</span><a href="http://it.tovrella.net">it.tovrella.net</a>
    </p>
    <p>
      <a href="http://us.ridepennon.eu">us.ridepennon.eu</a><span class="sep">|</span><a href="http://fr.ridepennon.eu">fr.ridepennon.eu</a><br>
      <a href="http://es.ridepennon.eu">es.ridepennon.eu</a><span class="sep">|</span><a href="http://de.ridepennon.eu">de.ridepennon.eu</a>
    </p>
  </div>

  <h2 class="section-title video-title">Watch Our Video</h2>
  <div class="video-frame">
    <div class="video-still" role="img" aria-label="Video still of a flag mounted on a car bonnet">
      <svg class="play-button" width="88" height="88" viewBox="0 0 88 88" aria-hidden="true">
        <circle cx="44" cy="44" r="41" fill="rgba(0,0,0,0.35)" stroke="#fff" stroke-width="4"/>
        <path d="M35 28 L62 44 L35 60 Z" fill="#fff"/>
      </svg>
    </div>
  </div>

  <section class="shop-logos">
    <a class="shop-logo envoy" href="http://www.envoy-pennon.com">EnvoyPennon</a>
    <a class="shop-logo ride" href="http://www.ridepennon.eu"><span class="mark"></span>ridepennon.eu</a>
    <a class="shop-logo tov" href="http://www.tovrella.ne/">tovRella</a>
  </section>

  <footer class="footer">
    <div class="footer-links"><a href="#">Home</a><span class="sep">|</span><a href="#">Customer Service</a><span class="sep">|</span><a href="#">Impressum</a></div>
    <div class="footer-links">
      <a href="http://www.ridepennon.eu">www.ridepennon.eu</a><span class="sep">|</span>
      <a href="http://www.ridepennon.net">www.ridepennon.net</a><span class="sep">|</span>
      <a href="http://www.ridepennant.co.uk">www.ridepennant.co.uk</a><span class="sep">|</span>
      <a href="http://www.wagen-wimpel.net">www.wagen-wimpel.net</a><span class="sep">|</span>
      <a href="http://www.wagen-banner.at">www.wagen-banner.at</a><span class="sep">|</span>
      <a href="http://www.wagen-wimpl.ch">www.wagen-wimpl.ch</a>
    </div>
    <div class="footer-links"><a href="#">Site Map</a><span class="sep">|</span><a href="#">Search Terms</a><span class="sep">|</span><a href="#">Advanced Search</a><span class="sep">|</span><a href="#">Orders &amp; Returns</a><span class="sep">|</span><a href="#">Contact Us</a><span class="sep">|</span><a href="#">RSS</a></div>
    <div class="footer-note">Help Us to Keep Stackora Healthy - Report All Bugs (ver. 1.7.0.2)<br>© 2013 tovRella GmbH</div>
  </footer>
</div>
</body>
</html>
```